Bright Harbor Notes Wordpress Blog

I need to design a WordPress blog page. The name of the Blog is "Bright Harbor Notes". I am hoping for a simple design that is easy for me to post future posts to. I like the color teal for this. The website is brightharbornotes.example where I am going to write a personal blog. I don't have a logo for this, but am hoping for a header that has some swirly, but classy looking text. Easy on the eyes. The website will only have a couple of pages - the home landing page, and an about me page.

Font styles to use
Script

Colors
00a990
86cfc6
cfeae6

Requirements
Must have
• A header for the landing page of the blog. Clean layout of where the blog posts will lie.

```html
<!DOCTYPE html>
<html lang="en">
<head>
<meta charset="utf-8">
<title>Bright Harbor Notes</title>
<link href="https://fonts.googleapis.com/css2?family=Great+Vibes&family=Raleway:wght@400;500;600;700;800&family=Open+Sans:ital,wght@0,400;0,600;0,700;1,400&display=swap" rel="stylesheet">
<style>
:root{
  --teal:#00a990;
  --teal-dark:#00806d;
  --teal-soft:#86cfc6;
  --teal-tint:#cfeae6;
  --ink:#2b2b2b;
  --body:#6e6e6e;
  --muted:#9a9a9a;
  --line:#e6e6e6;
  --dark:#2e2e2e;
  --navy:#0b1326;
  --gold:#f2b705;
  --white:#ffffff;
}
*{margin:0;padding:0;box-sizing:border-box}
html,body{width:1200px;height:2403px;overflow:hidden;background:var(--white)}
body{position:relative;font-family:"Open Sans",Arial,sans-serif;color:var(--body)}
a{text-decoration:none}

/* header */
.site-header{position:absolute;left:0;top:0;width:1200px;height:112px;background:var(--white)}
.brand{position:absolute;left:131px;top:26px;height:60px;display:flex;align-items:center;gap:16px}
.brand-mark{width:58px;height:58px;border-radius:50%;background:var(--teal-soft)}
.brand-name{font-family:"Great Vibes",cursive;font-weight:400;font-size:38px;color:var(--teal);line-height:1;white-space:nowrap}
.nav a{position:absolute;top:0;height:112px;line-height:112px;font-family:"Raleway",sans-serif;font-weight:600;font-size:14px;color:var(--ink)}
.nav .active{left:572px;width:90px;background:var(--teal);color:var(--white);text-align:center}
.btn{display:inline-block;background:var(--teal-dark);color:var(--white);font-family:"Raleway",sans-serif;font-weight:600;border-radius:20px;text-align:center}
.quote-btn{position:absolute;left:940px;top:37px;width:127px;height:38px;line-height:38px;font-size:14px}

/* hero */
.hero{position:absolute;left:0;top:112px;width:1200px;height:537px;overflow:hidden}
.hero-photo{position:absolute;inset:0;background:radial-gradient(circle at 28% 35%,#3a5f93 0%,#16284a 30%,var(--navy) 65%)}
.hero-copy{position:absolute;left:719px;top:136px;color:var(--white)}
.hero-copy h1{font-family:"Raleway",sans-serif;font-weight:800;font-size:35px;letter-spacing:.5px}
.hero-copy p{font-family:"Raleway",sans-serif;font-size:17px;line-height:36px;margin-top:6px}
.hero-btn{position:absolute;left:722px;top:280px;width:143px;height:38px;line-height:38px;font-size:14px;background:var(--teal)}
.dots{position:absolute;top:382px;left:989px;display:flex;gap:17px}
.dots span{width:14px;height:14px;border-radius:50%;border:2px solid var(--white)}
.dots .on{background:var(--teal);border-color:var(--teal-soft)}
.hero-wave{position:absolute;left:0;bottom:0;width:1200px;height:110px}

/* blog */
.section-title{position:absolute;font-family:"Raleway",sans-serif;font-weight:500;font-size:26px;color:var(--ink)}
.title-rule{position:absolute;height:2px;background:var(--line)}
.title-rule i{display:block;width:62px;height:3px;background:var(--teal)}
.view-all{position:absolute;left:676px;top:700px;font-size:11px;color:var(--teal)}
.blog-divider{position:absolute;left:775px;top:695px;width:1px;height:1072px;background:var(--line)}
.post{position:absolute;left:131px;width:644px;height:205px}
.post-photo{position:absolute;left:0;top:0;width:268px;height:205px}
.post-body{position:absolute;left:290px;top:0;width:345px}
.post-title{font-family:"Raleway",sans-serif;font-weight:600;font-size:14px;color:var(--ink);margin-top:-2px}
.rating{margin-top:8px;font-size:12px;color:var(--muted);font-style:italic}
.rating b{color:var(--gold);font-style:normal;letter-spacing:-1px;margin-right:6px;font-size:13px}
.excerpt{margin-top:7px;font-size:10.5px;line-height:24px;color:var(--body)}
.excerpt em{font-style:normal;color:var(--teal)}
.share{margin-top:6px;font-size:10.5px;color:var(--muted);display:flex;align-items:center;gap:24px}
.share span{width:7px;height:7px;border-radius:50%;background:var(--teal)}
.share span:first-of-type{margin-left:-4px}
.post-meta{position:absolute;top:168px;display:flex;align-items:center;font-size:11px;color:var(--teal)}
.post-meta .stat{display:flex;align-items:center;gap:4px;padding-right:12px}
.post-meta .stat+.stat{border-left:1px solid var(--line);padding-left:8px}
.date-pill{position:absolute;left:104px;top:-12px;width:164px;height:39px;border:1.5px solid var(--teal);border-radius:20px;line-height:36px;text-align:center;font-family:"Raleway",sans-serif;font-weight:700;font-size:10px;color:var(--teal);white-space:nowrap}
.post-rule{position:absolute;left:131px;width:644px;height:1px;background:var(--line)}

/* sidebar */
.widget{position:absolute;left:812px;width:255px;border:1px solid var(--line);background:var(--white)}
.widget-head{height:50px;line-height:50px;background:var(--dark);color:var(--white);text-align:center;font-family:"Raleway",sans-serif;font-weight:600;font-size:17px}
.testimonial{top:697px;height:344px;text-align:center}
.testimonial h3{margin-top:26px;font-family:"Raleway",sans-serif;font-weight:500;font-size:17px;color:var(--ink)}
.avatar{width:86px;height:86px;border-radius:50%;margin:18px auto 0;border:3px solid var(--teal-tint);background:radial-gradient(circle at 50% 40%,#e7b59c,#b2704f 60%,#6a3a26)}
.testimonial .who{margin-top:14px;font-size:12px;color:var(--teal)}
.testimonial blockquote{margin:8px 28px 0;font-size:10.5px;line-height:24px;font-style:italic;color:var(--body)}
.t-social{display:flex;justify-content:center;gap:9px;margin-top:10px}
.t-social span{width:25px;height:25px;border-radius:50%}
.popular{top:1062px;height:324px}
.pop-item{position:absolute;left:12px;width:232px;height:64px}
.pop-thumb{position:absolute;left:0;top:0;width:76px;height:64px}
.pop-text{position:absolute;left:89px;top:3px;font-size:11px;line-height:18px;color:var(--body);white-space:nowrap}
.pop-text span{color:var(--teal)}
.newsletter{top:1407px;height:265px;text-align:center}
.newsletter p{margin:18px 18px 0;font-size:11px;line-height:19px;color:var(--body)}
.field{margin:12px auto 0;width:232px;height:36px;border:1px solid var(--line);display:flex;align-items:center;justify-content:space-between;padding:0 12px;font-size:10.5px;color:var(--muted)}
.field+.field{margin-top:9px}
.sign-btn{margin-top:14px;width:115px;height:35px;line-height:35px;font-size:11px;font-weight:700;border-radius:18px}

/* about band */
.about-band{position:absolute;left:0;top:1828px;width:1200px;height:288px;background:linear-gradient(180deg,#3a3d42 0%,#2c2f33 55%,#3d3122 100%);text-align:center;color:var(--white)}
.about-band h2{margin-top:44px;font-family:"Raleway",sans-serif;font-weight:500;font-size:26px}
.about-band .rule{width:116px;height:2px;background:var(--teal-soft);margin:8px auto 0}
.about-band p{width:850px;margin:18px auto 0;font-size:12px;line-height:25px}
.about-btn{margin-top:14px;width:143px;height:37px;line-height:37px;font-size:14px;background:var(--teal)}

/* footer */
.site-footer{position:absolute;left:0;top:2116px;width:1200px;height:287px;background:var(--white)}
.f-col{position:absolute;top:42px}
.f-col h4{font-family:"Raleway",sans-serif;font-weight:500;font-size:17px;color:#555}
.f-col ul{list-style:none;margin-top:20px;font-size:11px;color:#666;line-height:24px}
.f-sep{position:absolute;top:40px;width:1px;height:146px;background:var(--line)}
.contact li{display:flex;gap:10px;align-items:flex-start;margin-bottom:10px;line-height:19px}
.contact svg{flex:none;margin-top:3px}
.follow{display:grid;grid-template-columns:repeat(3,24px);gap:16px 16px;margin-top:22px}
.follow span{width:24px;height:24px;border-radius:50%;background:#6b6b6b}
.foot-rule{position:absolute;left:131px;top:223px;width:936px;height:1px;background:var(--line)}
.copyright{position:absolute;top:248px;left:0;width:1200px;text-align:center;font-size:11px;color:#666}
</style>
</head>
<body>

<header class="site-header">
  <div class="brand"><span class="brand-mark"></span><span class="brand-name">Bright Harbor Notes</span></div>
  <nav class="nav">
    <a class="active" href="#">Home</a>
    <a href="#" style="left:696px">About Nora</a>
    <a href="#" style="left:835px">Contact</a>
  </nav>
  <a class="btn quote-btn" href="#">Get a Quote</a>
</header>

<section class="hero">
  <div class="hero-photo" role="img" aria-label="Glowing wireframe light bulb floating above an open hand on a dark blue network background"></div>
  <div class="hero-copy">
    <h1>PERSONAL GROWTH</h1>
    <p>Architecto beatae vitae dicta sunt explicabo<br>Nemo enim ipsam voluptatem...</p>
  </div>
  <a class="btn hero-btn" href="#">Learn More Info</a>
  <div class="dots"><span class="on"></span><span></span><span></span></div>
  <svg class="hero-wave" viewBox="0 0 1200 110" preserveAspectRatio="none">
    <path d="M0 34 C260 110 560 30 800 8 C960 -4 1100 10 1200 34 L1200 110 L0 110 Z" fill="var(--teal)"/>
    <path d="M0 78 C260 110 560 52 800 30 C960 18 1100 26 1200 44 L1200 110 L0 110 Z" fill="var(--white)"/>
  </svg>
</section>

<main>
  <h2 class="section-title" style="left:131px;top:689px">Recent Blog Posts</h2>
  <div class="title-rule" style="left:131px;top:728px;width:178px"><i></i></div>
  <a class="view-all" href="#">View All Posts &gt;&gt;</a>
  <div class="blog-divider"></div>

  <article class="post" style="top:769px">
    <div class="post-photo" role="img" aria-label="Small wooden figures in a row on a shelf with a hand lifting one higher" style="background:linear-gradient(135deg,#7a3d2a,#4e2218 60%,#8a5a44)"></div>
    <div class="post-body">
      <h3 class="post-title">Cupidatat non proident, sunt ipsam...</h3>
      <div class="rating"><b>★★★★★</b>(134 Reviews)</div>
      <p class="excerpt">Adipisci velit, sed quia non numquam eius modi tempora incidunt ut labore et dolore magnam aliquam quaerat voluptatem. Ut enim nem ullam corporis suscipit..<em>Read More+</em></p>
      <div class="share">Share With : <span></span><span></span><span></span><span></span><span></span></div>
    </div>
    <div class="post-meta" style="left:290px">
      <div class="stat"><svg width="14" height="13" viewBox="0 0 24 22"><path d="M12 21 C5 15 1 11 1 6.5 A5.5 5.5 0 0 1 12 4 A5.5 5.5 0 0 1 23 6.5 C23 11 19 15 12 21Z" fill="none" stroke="var(--teal)" stroke-width="2"/></svg>23</div>
      <div class="stat"><svg width="14" height="13" viewBox="0 0 24 22"><path d="M3 3 H21 V15 H9 L4 20 V15 H3Z" fill="none" stroke="var(--teal)" stroke-width="2" stroke-linejoin="round"/></svg>12</div>
      <div class="date-pill">POST ON 23 MARCH 2017</div>
    </div>
  </article>
  <div class="post-rule" style="top:1004px"></div>

  <article class="post" style="top:1033px">
    <div class="post-photo" role="img" aria-label="Football hitting the net of a goal under stadium lights" style="background:linear-gradient(180deg,#5a4a5e,#2b2b35 45%,#2f6a2a)"></div>
    <div class="post-body">
      <h3 class="post-title">Cupidatat non proident, sunt ipsam...</h3>
      <div class="rating"><b>★★★★★</b>(134 Reviews)</div>
      <p class="excerpt">Adipisci velit, sed quia non numquam eius modi tempora incidunt ut labore et dolore magnam aliquam quaerat voluptatem. Ut enim nem ullam corporis suscipit..<em>Read More+</em></p>
      <div class="share">Share With : <span></span><span></span><span></span><span></span><span></span></div>
    </div>
    <div class="post-meta" style="left:290px">
      <div class="stat"><svg width="14" height="13" viewBox="0 0 24 22"><path d="M12 21 C5 15 1 11 1 6.5 A5.5 5.5 0 0 1 12 4 A5.5 5.5 0 0 1 23 6.5 C23 11 19 15 12 21Z" fill="none" stroke="var(--teal)" stroke-width="2"/></svg>23</div>
      <div class="stat"><svg width="14" height="13" viewBox="0 0 24 22"><path d="M3 3 H21 V15 H9 L4 20 V15 H3Z" fill="none" stroke="var(--teal)" stroke-width="2" stroke-linejoin="round"/></svg>12</div>
      <div class="date-pill">POST ON 23 MARCH 2017</div>
    </div>
  </article>
  <div class="post-rule" style="top:1268px"></div>

  <article class="post" style="top:1297px">
    <div class="post-photo" role="img" aria-label="Archer aiming a bow at a target on a salt flat under a blue sky" style="background:linear-gradient(180deg,#5f95b6,#a9c6d4 50%,#e0dcd2)"></div>
    <div class="post-body">
      <h3 class="post-title">Cupidatat non proident, sunt ipsam...</h3>
      <div class="rating"><b>★★★★★</b>(134 Reviews)</div>
      <p class="excerpt">Adipisci velit, sed quia non numquam eius modi tempora incidunt ut labore et dolore magnam aliquam quaerat voluptatem. Ut enim nem ullam corporis suscipit..<em>Read More+</em></p>
      <div class="share">Share With : <span></span><span></span><span></span><span></span><span></span></div>
    </div>
    <div class="post-meta" style="left:290px">
      <div class="stat"><svg width="14" height="13" viewBox="0 0 24 22"><path d="M12 21 C5 15 1 11 1 6.5 A5.5 5.5 0 0 1 12 4 A5.5 5.5 0 0 1 23 6.5 C23 11 19 15 12 21Z" fill="none" stroke="var(--teal)" stroke-width="2"/></svg>23</div>
      <div class="stat"><svg width="14" height="13" viewBox="0 0 24 22"><path d="M3 3 H21 V15 H9 L4 20 V15 H3Z" fill="none" stroke="var(--teal)" stroke-width="2" stroke-linejoin="round"/></svg>12</div>
      <div class="date-pill">POST ON 23 MARCH 2017</div>
    </div>
  </article>
  <div class="post-rule" style="top:1532px"></div>

  <article class="post" style="top:1561px">
    <div class="post-photo" role="img" aria-label="Hiker with raised arms on a mountain peak above the clouds at sunrise" style="background:linear-gradient(180deg,#1f5fa8,#7fa9d0 45%,#d7d9dc 70%,#6e5a3c)"></div>
    <div class="post-body">
      <h3 class="post-title">Cupidatat non proident, sunt ipsam...</h3>
      <div class="rating"><b>★★★★★</b>(134 Reviews)</div>
      <p class="excerpt">Adipisci velit, sed quia non numquam eius modi tempora incidunt ut labore et dolore magnam aliquam quaerat voluptatem. Ut enim nem ullam corporis suscipit..<em>Read More+</em></p>
      <div class="share">Share With : <span></span><span></span><span></span><span></span><span></span></div>
    </div>
    <div class="post-meta" style="left:290px">
      <div class="stat"><svg width="14" height="13" viewBox="0 0 24 22"><path d="M12 21 C5 15 1 11 1 6.5 A5.5 5.5 0 0 1 12 4 A5.5 5.5 0 0 1 23 6.5 C23 11 19 15 12 21Z" fill="none" stroke="var(--teal)" stroke-width="2"/></svg>23</div>
      <div class="stat"><svg width="14" height="13" viewBox="0 0 24 22"><path d="M3 3 H21 V15 H9 L4 20 V15 H3Z" fill="none" stroke="var(--teal)" stroke-width="2" stroke-linejoin="round"/></svg>12</div>
      <div class="date-pill">POST ON 23 MARCH 2017</div>
    </div>
  </article>

  <aside>
    <section class="widget testimonial">
      <h3>What People Say's</h3>
      <div class="avatar" role="img" aria-label="Portrait photo of the reviewer"></div>
      <div class="who">-Ella Marsh</div>
      <blockquote>“ Ratione voluptatem sequi nesciunt. Neque porro quisquam est, qui dolorem ipsum quia dolor sit amet, consectetur, adipisci velit...</blockquote>
      <div class="t-social"><span style="background:var(--teal)"></span><span style="background:var(--teal-soft)"></span></div>
    </section>

    <section class="widget popular">
      <div class="widget-head">Popular Posts</div>
      <div class="pop-item" style="top:74px">
        <div class="pop-thumb" role="img" aria-label="Businessman standing in a warm lit office" style="background:linear-gradient(135deg,#b58a63,#5a3a2a)"></div>
        <div class="pop-text">Explicabo. Nem ipsam vou<br>platem quia..<br><span>23 March,2017</span></div>
      </div>
      <div class="pop-item" style="top:154px">
        <div class="pop-thumb" role="img" aria-label="Dart in a target on a dark background" style="background:linear-gradient(135deg,#555,#1c1c1c)"></div>
        <div class="pop-text">Explicabo. Nem ipsam vou<br>platem quia..<br><span>23 March,2017</span></div>
      </div>
      <div class="pop-item" style="top:234px">
        <div class="pop-thumb" role="img" aria-label="Person in red cape against a bright sky" style="background:linear-gradient(135deg,#e9c9a6,#b8322c)"></div>
        <div class="pop-text">Explicabo. Nem ipsam vou<br>platem quia..<br><span>23 March,2017</span></div>
      </div>
    </section>

    <section class="widget newsletter">
      <div class="widget-head">Newsletter</div>
      <p>Numquam eius modi tempora incidunt<br>culpa qui officia..</p>
      <div class="field">Enter Your Name<svg width="10" height="11" viewBox="0 0 10 11"><circle cx="5" cy="3" r="2.6" fill="#999"/><path d="M0 11 C0 7 10 7 10 11Z" fill="#999"/></svg></div>
      <div class="field">Enter Your Email<svg width="11" height="8" viewBox="0 0 11 8"><rect width="11" height="8" fill="#999"/><path d="M0 0 L5.5 4.5 L11 0" fill="none" stroke="#fff"/></svg></div>
      <a class="btn sign-btn" href="#">SIGN UP</a>
    </section>
  </aside>
</main>

<section class="about-band" role="img" aria-label="Dim city skyline at dusk behind the about section">
  <h2>About Nora</h2>
  <div class="rule"></div>
  <p>Nam libero tempore, cum soluta nobis est eligendi optio cumque nihil impedit quo minus id quod maxime placeat facere possimus, omnis voluptas assumenda est, omnis dolor repellendus. Temporibus autem quibusdam et aut officiis debitis aut saepe eveniet ut et voluptates repudiandae sint et molestiae non recusandaerum...</p>
  <a class="btn about-btn" href="#">Learn More Info</a>
</section>

<footer class="site-footer">
  <div class="f-col" style="left:131px"><h4>Quick Links</h4><ul><li>Home</li><li>About Nora</li><li>Contact</li></ul></div>
  <div class="f-sep" style="left:285px"></div>
  <div class="f-col" style="left:346px"><h4>Information</h4><ul><li>Terms &amp; Conditions</li><li>Privacy Policy</li><li>Disclaimer</li><li>Site map</li></ul></div>
  <div class="f-sep" style="left:525px"></div>
  <div class="f-col contact" style="left:596px"><h4>Contact Info</h4>
    <ul>
      <li><svg width="11" height="14" viewBox="0 0 11 14"><path d="M5.5 13.5 C2 9 1 7 1 5 A4.5 4.5 0 0 1 10 5 C10 7 9 9 5.5 13.5Z" fill="none" stroke="#888"/><circle cx="5.5" cy="5" r="1.6" fill="none" stroke="#888"/></svg><span>45 Bright Harbor Notes Company,<br>Street Name, City-454</span></li>
      <li><svg width="13" height="13" viewBox="0 0 13 13"><path d="M2 1 L4.5 1 L5.5 4 L4 5 C5 7 6 8 8 9 L9 7.5 L12 8.5 L12 11 C12 12 11 12.5 10 12 C5 11 2 8 1 3 C0.8 2 1 1 2 1Z" fill="none" stroke="#888"/></svg><span>Phone : (+345) 555-0142</span></li>
      <li><svg width="13" height="10" viewBox="0 0 13 10"><rect x=".5" y=".5" width="12" height="9" fill="none" stroke="#888"/><path d="M.5 .5 L6.5 5.5 L12.5 .5" fill="none" stroke="#888"/></svg><span>Email : info@brightharbornotes.example</span></li>
    </ul>
  </div>
  <div class="f-sep" style="left:892px"></div>
  <div class="f-col" style="left:960px"><h4>Follow Us</h4>
    <div class="follow"><span></span><span></span><span></span><span></span><span></span></div>
  </div>
  <div class="foot-rule"></div>
  <p class="copyright">Copyrights © brightharbornotes.example . 2017 | Allrights Reserved.</p>
</footer>

</body>
</html>
```